HARPINE - Harwell Clerical Solutions, Inc./Pinecrest Mailing Works, Inc. Needs a Letterhead Desig

Letterhead - thoughts 2 files uploaded 1 is the current letterhead and only change to the words is message at bottom - should be 25 Years of Industry Experience

2nd file is so that you can see how top of letterhead was before changes - had graphic bleed which we liked.

Goal for letterhead - we're a print / mail shop so we need a look that fits with agencies. I would like a bit of a square font for address, phone, email info otherwise be creative. We like a blue 307 and would like to incorporate a little green or tan.

```html
<!DOCTYPE html>
<html lang="en">
<head>
<meta charset="utf-8">
<title>Harwell Clerical Solutions &amp; Pinecrest Mailing Works Letterhead</title>
<link href="https://fonts.googleapis.com/css2?family=Archivo:wght@700;800&family=Jost:wght@300;600&display=swap" rel="stylesheet">
<style>
  :root {
    --brand-blue: #0057a3;
    --brand-green: #4c9f2a;
    --paper: #ffffff;
  }
  * { margin: 0; padding: 0; box-sizing: border-box; }
  html, body { width: 944px; height: 1200px; overflow: hidden; background: var(--paper); }
  .letterhead { position: relative; width: 944px; height: 1200px; background: var(--paper); overflow: hidden; }

  .company-marks { position: absolute; top: 28px; left: 12px; display: flex; gap: 34px; align-items: center; }
  .company-name {
    display: flex; align-items: center; gap: 8px;
    font-family: "Archivo", Arial, sans-serif; font-weight: 800;
    font-size: 17px; color: var(--brand-blue); letter-spacing: 0.2px;
  }
  .company-name .mark-square { width: 14px; height: 14px; background: var(--brand-blue); flex: none; }

  .footer-shapes { position: absolute; left: 0; top: 0; width: 944px; height: 1200px; }

  .footer-info { position: absolute; left: 10px; top: 993px; color: var(--paper); }
  .tagline {
    font-family: "Archivo", Arial, sans-serif; font-weight: 700;
    font-size: 22px; color: var(--brand-blue); margin-bottom: 5px; letter-spacing: -0.3px;
    white-space: nowrap;
  }
  .tagline .years { font-family: "Jost", sans-serif; font-weight: 600; font-size: 25px; margin-right: 3px; }
  .contact-line {
    font-family: "Jost", "Futura", sans-serif; font-weight: 300;
    font-size: 20px; line-height: 32.8px; text-transform: uppercase; letter-spacing: 0.3px;
    white-space: nowrap;
  }
</style>
</head>
<body>
<div class="letterhead">
  <header class="company-marks">
    <div class="company-name"><span class="mark-square"></span>Harwell Clerical Solutions, Inc.</div>
    <div class="company-name">Pinecrest Mailing Works, Inc.</div>
  </header>

  <svg class="footer-shapes" viewBox="0 0 944 1200" aria-hidden="true">
    <polygon points="0,903 944,1160 944,1200 0,1200" fill="var(--brand-green)"/>
    <polygon points="0,903 595,1066 0,1066" fill="var(--brand-green)"/>
    <polygon points="944,902 595,1066 944,1160" fill="var(--brand-blue)"/>
  </svg>

  <footer class="footer-info">
    <p class="tagline"><span class="years">25</span> Years of Industry Experience</p>
    <p class="contact-line">4218 W.Aldergate</p>
    <p class="contact-line">Millbrook,IL60412</p>
    <p class="contact-line">Ph:312-555-0148</p>
    <p class="contact-line">Fax:312-555-0193</p>
    <p class="contact-line">Email:customerservice@harpine.com</p>
  </footer>
</div>
</body>
</html>
```